Release Therapy business card that deals with the release of negative issues

I need a business card for my business called MEADOWS (A gentle shore to rest when you drift) ... I'm a therapist that deals with people releasing negative issues, by applying therapies that incorporate, hypnosis, aromatherapy and listen therapy..I like the colour green and soft blues...My idea is for a hand releasing butterflies, and incorporating soft clouds....
Target Market(s)
All people, all ages
Industry/Entity Type
Business
Contact Information for Business Card
MEADOWS"A Gentle Shore To Rest When You Drift"Yvette R BrockingtonRelease Therapist0411 743 781email: easingpaths4everyone@fernmail.example
Requirements
Must have
- butterflies and soft clouds
Nice to have
- I like the decorative and script fonts for business name, and also my name
- Marlene T Ashcombe...

```html
<!DOCTYPE html>
<html lang="en">
<head>
<meta charset="utf-8">
<title>MEADOWS – Business Card</title>
<link href="https://fonts.googleapis.com/css2?family=Questrial&family=Pinyon+Script&display=swap" rel="stylesheet">
<style>
  :root {
    --stage: #e7e7e9;
    --sky: #bfe3f1;
    --sky-deep: #9fd3ea;
    --mist: #f4f9fa;
    --meadow-tint: #e3f3e6;
    --teal: #3aa7c8;
    --teal-dark: #2b8fb0;
    --leaf: #8cc63f;
    --ink-script: #2c7f9c;
    --release-blue: rgba(120, 178, 210, 0.55);
    --release-green: rgba(160, 210, 170, 0.45);
    --shadow: rgba(60, 70, 80, 0.18);
  }
  * { margin: 0; padding: 0; box-sizing: border-box; }
  html, body { width: 1200px; height: 848px; overflow: hidden; }
  body {
    background: var(--stage);
    font-family: "Questrial", sans-serif;
    position: relative;
  }
  .card {
    position: absolute;
    width: 560px;
    height: 320px;
    overflow: hidden;
    box-shadow: 0 6px 18px var(--shadow);
    background:
      radial-gradient(ellipse 60% 45% at 25% 20%, var(--sky-deep), transparent 70%),
      radial-gradient(ellipse 55% 40% at 80% 15%, var(--sky), transparent 70%),
      radial-gradient(ellipse 70% 40% at 50% 60%, var(--mist), transparent 75%),
      radial-gradient(ellipse 60% 35% at 85% 85%, var(--meadow-tint), transparent 70%),
      linear-gradient(180deg, var(--sky) 0%, var(--mist) 60%, var(--meadow-tint) 100%);
  }
  .card--front { left: 80px; top: 90px; }
  .card--back { left: 560px; top: 430px; }

  .brand { display: flex; align-items: center; gap: 12px; }
  .brand__dot {
    width: 22px; height: 22px; border-radius: 50%;
    background: var(--teal);
  }
  .brand__name {
    color: var(--teal);
    font-family: "Questrial", sans-serif;
    letter-spacing: 4px;
  }
  .tagline { color: var(--teal-dark); font-size: 14px; letter-spacing: 0.3px; }

  .card--front .brand-lockup {
    position: absolute; left: 120px; top: 105px;
    display: flex; flex-direction: column; align-items: flex-start; gap: 10px;
  }
  .card--front .brand__name { font-size: 52px; }

  .card--back .brand-lockup {
    position: absolute; left: 34px; top: 40px;
    display: flex; flex-direction: column; gap: 5px;
  }
  .card--back .brand__dot { width: 14px; height: 14px; }
  .card--back .brand__name { font-size: 28px; letter-spacing: 3px; }
  .card--back .tagline { font-size: 10px; }

  .decor-release {
    position: absolute; right: 0; top: 0;
    width: 320px; height: 320px;
    background:
      radial-gradient(ellipse closest-side at 62% 68%, var(--release-blue), transparent),
      radial-gradient(ellipse closest-side at 55% 38%, var(--release-green), transparent);
  }

  .person { position: absolute; left: 38px; top: 122px; }
  .person__name {
    font-family: "Pinyon Script", cursive;
    color: var(--ink-script);
    font-size: 38px;
    line-height: 1.1;
  }
  .person__role { color: var(--leaf); font-size: 20px; margin-top: 2px; }

  .contact {
    position: absolute; left: 40px; top: 228px;
    color: var(--teal); font-size: 17px; line-height: 1.55;
  }
</style>
</head>
<body>

  <section class="card card--front" aria-label="Business card front">
    <div class="brand-lockup">
      <div class="brand">
        <span class="brand__dot"></span>
        <span class="brand__name">MEADOWS</span>
      </div>
      <p class="tagline">A Gentle Shore To Rest When You Drift</p>
    </div>
  </section>

  <section class="card card--back" aria-label="Business card back">
    <div class="decor-release" role="img" aria-label="Faint illustration of an open hand releasing butterflies"></div>

    <div class="brand-lockup">
      <div class="brand">
        <span class="brand__dot"></span>
        <span class="brand__name">MEADOWS</span>
      </div>
      <p class="tagline">A Gentle Shore To Rest When You Drift</p>
    </div>

    <div class="person">
      <p class="person__name">Marlene T Ashcombe</p>
      <p class="person__role">Release Therapist</p>
    </div>

    <div class="contact">
      <p class="contact__phone">0452 186 930</p>
      <p class="contact__email">easingpaths4everyone@fernmail.example</p>
    </div>
  </section>

</body>
</html>
```